Easy Business Card / Presentation Cover Design Project

We are looking for a business card design, covers for powerpoint presentations for investors, and possibly simple stationary for a Chicago real estate development firm. Our new logo is attached below.

We rehab and provide newly constructed homes. We are not a real estate brokerage firm (i.e., agents such as Meridale 47) and only operate in the Chicago area.

In terms of design, sophisticated and high end that would appeal to investors (theme should resemble investment banks, hedge funds, private equity rather than tech startup).

Target Market(s)

Investors, banks, financing sources

Industry/Entity Type

Real Estate

Requirements
Must have
• Two deliverables here. 1) Business card 2) Covers for powerpoint presentation.

Must be able to look sophisticated and high end when printed. Please think through the type of printing that will be needed. Would prefer something that can be printed in raised ink but digital is ok as well.

Will be printed on heavy paper.

Business Card: Horizontal Layout, no black backgrounds,

For presentation front cover, should include logo only. For back cover, should include contact info. Horizontal and should not contain any information that will need to be changed (i.e. date or client name)
Nice to have
• Would like to have the edges colored but not required. Please show multiple designs
Should not have
• Should not have any die cut or embossed type of designs. Shape should be standard size.

We are not a design firm, a retail firm, or a consumer product firm.

Please do not incorporate a house, buildings, etc. This must be very professional looking.

```html
<!DOCTYPE html>
<html lang="en">
<head>
<meta charset="utf-8">
<title>Velmont Realty – Business Card</title>
<link rel="stylesheet" href="https://fonts.googleapis.com/css2?family=Tinos:wght@400;700&family=Arimo:wght@400&display=swap">
<style>
  :root {
    --page-bg: #ece9e4;
    --card-grey: #c8cacd;
    --card-light: #ffffff;
    --band-grey: #8c8f93;
    --brand-blue: #1a8cf0;
    --brand-blue-light: #35b4ff;
    --brand-blue-deep: #0f6fd6;
    --ink: #1b1b1d;
    --ink-soft: #4a4c50;
    --ink-muted: #6d7075;
  }
  * { margin: 0; padding: 0; box-sizing: border-box; }
  html, body { width: 1200px; height: 1000px; overflow: hidden; }
  body {
    background: var(--page-bg);
    position: relative;
    font-family: "Arimo", Arial, sans-serif;
  }
  .card {
    position: absolute;
    left: 250px;
    width: 700px;
    height: 400px;
    overflow: hidden;
    box-shadow: 0 6px 18px rgba(0,0,0,0.18);
  }
  .card--front { top: 60px; }
  .card--back { top: 540px; }
  .card__art { position: absolute; inset: 0; width: 100%; height: 100%; }

  .brand {
    position: absolute;
    display: flex;
    align-items: center;
    gap: 12px;
  }
  .brand__dot {
    width: 46px; height: 46px;
    border-radius: 50%;
    background: var(--brand-blue);
  }
  .brand__name {
    font-family: "Tinos", "Times New Roman", serif;
    font-weight: 400;
    font-size: 34px;
    color: var(--ink);
    letter-spacing: 0.5px;
  }
  .card--front .brand { left: 230px; top: 150px; }
  .card--back .brand { left: 40px; top: 40px; }
  .card--back .brand__name { font-size: 30px; }

  .contact {
    position: absolute;
    left: 40px;
    top: 160px;
    list-style: none;
    font-size: 15px;
    line-height: 20px;
    color: var(--ink-soft);
  }
  .holder {
    position: absolute;
    right: 44px;
    top: 208px;
    text-align: right;
  }
  .holder__name {
    font-family: "Tinos", "Times New Roman", serif;
    font-weight: 700;
    font-size: 27px;
    color: var(--ink);
    letter-spacing: 0.5px;
  }
  .holder__role {
    font-family: "Arimo", Arial, sans-serif;
    font-size: 17px;
    color: var(--ink-muted);
    letter-spacing: 1px;
    margin-top: 2px;
  }
</style>
</head>
<body>

<section class="card card--front" aria-label="Business card front">
  <svg class="card__art" viewBox="0 0 700 400" aria-hidden="true">
    <defs>
      <radialGradient id="front-glow" cx="0.6" cy="0.38" r="0.7">
        <stop offset="0" stop-color="var(--card-light)"/>
        <stop offset="0.45" stop-color="#e6e7e9"/>
        <stop offset="1" stop-color="var(--card-grey)"/>
      </radialGradient>
      <linearGradient id="front-blue" x1="0" y1="0" x2="1" y2="0">
        <stop offset="0" stop-color="var(--brand-blue-deep)"/>
        <stop offset="0.5" stop-color="var(--brand-blue)"/>
        <stop offset="1" stop-color="var(--brand-blue-light)"/>
      </linearGradient>
    </defs>
    <rect width="700" height="400" fill="url(#front-glow)"/>
    <path d="M0,282 Q330,262 700,196 L700,214 Q340,292 0,318 Z" fill="var(--band-grey)"/>
    <path d="M0,318 Q340,292 700,214 L700,400 L0,400 Z" fill="url(#front-blue)"/>
  </svg>
  <div class="brand">
    <span class="brand__dot"></span>
    <span class="brand__name">Velmont Realty</span>
  </div>
</section>

<section class="card card--back" aria-label="Business card back">
  <svg class="card__art" viewBox="0 0 700 400" aria-hidden="true">
    <defs>
      <radialGradient id="back-glow" cx="0.5" cy="0.4" r="0.7">
        <stop offset="0" stop-color="var(--card-light)"/>
        <stop offset="0.45" stop-color="#e4e5e7"/>
        <stop offset="1" stop-color="var(--card-grey)"/>
      </radialGradient>
      <linearGradient id="back-blue" x1="0" y1="0" x2="1" y2="0">
        <stop offset="0" stop-color="var(--brand-blue-light)"/>
        <stop offset="0.5" stop-color="var(--brand-blue)"/>
        <stop offset="1" stop-color="var(--brand-blue-deep)"/>
      </linearGradient>
    </defs>
    <rect width="700" height="400" fill="url(#back-glow)"/>
    <path d="M0,278 Q300,340 700,236 L700,256 Q320,362 0,308 Z" fill="var(--band-grey)"/>
    <path d="M0,308 Q320,362 700,256 L700,400 L0,400 Z" fill="url(#back-blue)"/>
  </svg>
  <div class="brand">
    <span class="brand__dot"></span>
    <span class="brand__name">Velmont Realty</span>
  </div>
  <ul class="contact">
    <li>Address:your address here</li>
    <li>E-mail:youremail@here.com</li>
    <li>Contact:your contact here</li>
    <li>Website:your website here</li>
  </ul>
  <div class="holder">
    <p class="holder__name">YOUR NAME HERE</p>
    <p class="holder__role">YOUR POSITION HERE</p>
  </div>
</section>

</body>
</html>
```